Modern Innovative Business Card Design

We require a nice, modern, clean business card design, ready for upload to Cardomora. Our company develops online banking software solutions for small financial insitutions. The design should be clean, professional, but yet not "corporate boring". See www.fyrolt.com for an idea of business image and profile. The design should communicate innovation, be modern and fresh, yet look professional and established.

Target Market(s)

Finance industry, bankers, entrepreneurs

Industry/Entity Type

Financial

Contact Information for Business Card

Tobias Wendlerup
CEO

FYROLT BV
Lindenwerf 38
1027 HX Amsterdam
The Netherlands

Phone: +31 20 517 8036
Direct: +31 20 604 1758
Skype: tobias.fyrolt
ceo@fyrolt.com
www.fyrolt.com

Font styles to use
Sans Serif

Requirements
Must have
• Should look clean, modern and professional. File should be ready for upload to cardomora.
Should not have
• Boring standard corporate layout

```html
<!DOCTYPE html>
<html lang="en">
<head>
<meta charset="utf-8">
<title>FYROLT business card</title>
<link rel="stylesheet" href="https://fonts.googleapis.com/css2?family=Open+Sans:wght@400;600;700&display=swap">
<style>
  :root {
    --backdrop: #e8e5e0;
    --paper: #ffffff;
    --charcoal: #3c3c3e;
    --charcoal-deep: #2c2c2e;
    --lime: #b4dc4a;
    --ink: #3a3a3a;
    --muted: #6a6a6a;
  }
  * { box-sizing: border-box; margin: 0; padding: 0; }
  html, body {
    width: 1200px; height: 1023px; overflow: hidden;
    background: var(--backdrop);
    font-family: "Open Sans", Arial, sans-serif;
  }
  .card {
    position: absolute; width: 700px; height: 400px;
    border-radius: 6px; overflow: hidden;
    box-shadow: 0 10px 30px rgba(0,0,0,.18);
  }
  /* front */
  .card-front { left: 60px; top: 70px; background: var(--paper); }
  .brand-name {
    position: absolute; left: 42px; top: 40px;
    font-size: 82px; font-weight: 600; letter-spacing: 4px;
    color: var(--charcoal); line-height: 1;
  }
  .person {
    position: absolute; left: 46px; top: 160px;
    font-size: 19px; font-variant: small-caps; letter-spacing: 2.5px;
    color: var(--ink);
  }
  .person .role { font-size: 14px; color: var(--muted); }
  .contact-band {
    position: absolute; left: 0; top: 205px; width: 520px; height: 88px;
    background: var(--lime);
    display: flex; gap: 60px; padding: 16px 0 0 46px;
  }
  .contact-list { list-style: none; font-size: 14px; color: var(--charcoal-deep); }
  .contact-list li { display: flex; align-items: center; gap: 8px; margin-bottom: 8px; }
  .contact-list svg { width: 13px; height: 13px; flex: none; }
  .chat-band {
    position: absolute; left: 0; top: 293px; width: 700px; height: 50px;
    background: var(--charcoal);
    display: flex; align-items: center; gap: 10px; padding-left: 330px;
    color: #fff; font-size: 15px;
  }
  .chat-dot { width: 22px; height: 22px; border-radius: 50%; background: #fff; }
  .address-panel {
    position: absolute; left: 505px; top: 28px; width: 195px; height: 265px;
    background: var(--charcoal);
    border-radius: 40px 0 0 0;
    padding: 22px 0 0 20px;
  }
  .address-box {
    background: var(--paper); border-radius: 28px 0 0 28px;
    height: 130px; padding: 26px 0 0 22px;
    font-size: 14px; line-height: 1.55; color: var(--muted);
  }
  /* back */
  .card-back {
    left: 440px; top: 560px;
    background: radial-gradient(ellipse at 40% 35%, #4a4a4c, var(--charcoal-deep) 80%);
    display: flex; align-items: center; justify-content: center;
  }
  .card-back .brand-name {
    position: static; color: #fff; font-size: 88px;
  }
</style>
</head>
<body>
  <section class="card card-front" aria-label="Business card front">
    <div class="brand-name">FYROLT</div>
    <p class="person">Tobias Wendlerup <span class="role">| CEO</span></p>

    <div class="contact-band">
      <ul class="contact-list">
        <li><svg viewBox="0 0 14 14"><rect width="14" height="14" rx="2" fill="#3c3c3e"/><path d="M4 3.5l2 2-1 1c.6 1.2 1.3 1.9 2.5 2.5l1-1 2 2-1 1.3C6.5 11 3 7.5 2.7 4.5z" fill="#fff"/></svg>+31 20 517 8036</li>
        <li><svg viewBox="0 0 14 14"><rect width="14" height="14" rx="2" fill="#3c3c3e"/><path d="M4 3.5l2 2-1 1c.6 1.2 1.3 1.9 2.5 2.5l1-1 2 2-1 1.3C6.5 11 3 7.5 2.7 4.5z" fill="#fff"/></svg>+31 20 604 1758</li>
      </ul>
      <ul class="contact-list">
        <li><svg viewBox="0 0 14 14"><rect width="14" height="14" rx="2" fill="#3c3c3e"/><path d="M3 4.5h8v5H3z M3 4.5l4 3 4-3" fill="none" stroke="#fff" stroke-width="1"/></svg>ceo@fyrolt.com</li>
        <li><svg viewBox="0 0 14 14"><rect width="14" height="14" rx="2" fill="#3c3c3e"/><circle cx="7" cy="7" r="4" fill="none" stroke="#fff"/><path d="M3 7h8M7 3v8" stroke="#fff" stroke-width=".8"/></svg>www.fyrolt.com</li>
      </ul>
    </div>

    <div class="chat-band">
      <span class="chat-dot"></span>
      <span class="chat-handle">tobias.fyrolt</span>
    </div>

    <div class="address-panel">
      <address class="address-box" style="font-style:normal">
        FYROLT BV<br>
        Lindenwerf 38<br>
        1027 HX Amsterdam<br>
        The Netherlands
      </address>
    </div>
  </section>

  <section class="card card-back" aria-label="Business card back">
    <div class="brand-name">FYROLT</div>
  </section>
</body>
</html>
```